Business Card Design

we pay more for your estate jewelry .

Industry/Entity Type

Jewelry

Contact Information for Business Card

ray's coin and bullion llc .we buy gold , silver ,coins and diamonds.742 willow creek road maple ridge vt 08099. 555-555-0148. open 7 days 9 to 7

```html
<!DOCTYPE html>
<html lang="en">
<head>
<meta charset="utf-8">
<title>Ray's Coin and Bullion llc – Business Cards</title>
<link rel="stylesheet" href="https://fonts.googleapis.com/css2?family=Arimo:wght@400;700&display=swap">
<style>
  :root {
    --page: #ffffff;
    --green-card: #0b780b;
    --green-edge: #2e4a2e;
    --charcoal: #363436;
    --charcoal-edge: #555355;
    --ink-dark: #1e1e1e;
    --cream: #ecdfa4;
    --pale: #dcdcdc;
    --grey-text: #a3a3a3;
    --shadow-band: #232323;
    --bright-green: #139a13;
    --white: #ffffff;
  }
  html, body {
    margin: 0;
    padding: 0;
    overflow: hidden;
    background: var(--page);
  }
  .canvas {
    position: relative;
    width: 1200px;
    height: 658px;
    background: var(--page);
    font-family: "Arimo", Arial, sans-serif;
  }
  .card {
    position: absolute;
    display: block;
    width: 562px;
    height: 331px;
  }
  .card--green { left: 638px; top: 0; }
  .card--charcoal { left: 0; top: 327px; }
  .card text { font-family: "Arimo", Arial, sans-serif; }
  .green-title { font-size: 26px; font-weight: 700; fill: var(--ink-dark); }
  .green-info { font-size: 14px; fill: var(--cream); }
  .green-phone { font-size: 20px; fill: var(--pale); }
  .hours { font-size: 12px; fill: var(--white); }
  .charcoal-title { font-size: 19px; fill: var(--grey-text); }
  .charcoal-info { font-size: 15.5px; fill: var(--grey-text); }
  .charcoal-phone { font-size: 20px; fill: var(--grey-text); }
</style>
</head>
<body>
<main class="canvas">

  <svg class="card card--green" viewBox="0 0 443 261" xmlns="http://www.w3.org/2000/svg" aria-label="Business card, green version">
    <defs>
      <linearGradient id="zigzag-dark" x1="0" y1="0" x2="1" y2="0">
        <stop offset="0" stop-color="#155515"/>
        <stop offset="1" stop-color="#1a6a1a" stop-opacity="0.6"/>
      </linearGradient>
    </defs>
    <rect class="card-face" x="0.75" y="0.75" width="441.5" height="259.5" fill="var(--green-card)" stroke="var(--green-edge)" stroke-width="1.5"/>
    <polygon class="zigzag" points="178,120 320,120 320,163 183,163 197,215 160,215 148,160" fill="url(#zigzag-dark)"/>
    <polygon class="base-band" points="1,212 155,215 192,260 1,260" fill="#1b331b"/>
    <polygon class="hours-corner" points="325,260 442,143 442,260" fill="var(--shadow-band)"/>
    <text class="green-title" x="222" y="45" text-anchor="middle">Ray's Coin and Bullion llc .</text>
    <text class="green-info" x="41" y="91">We buy Gold , Silver, Coins &amp; Diamonds.</text>
    <text class="green-info" x="41" y="109">742 Willow Creek road maple ridge vt 08099.</text>
    <text class="green-phone" x="17" y="249">555-555-0148.</text>
    <g transform="translate(398 222) rotate(-45)">
      <text class="hours" x="0" y="-4" text-anchor="middle">Open 7 days</text>
      <text class="hours" x="0" y="10" text-anchor="middle">9 to 7</text>
    </g>
  </svg>

  <svg class="card card--charcoal" viewBox="0 0 443 261" xmlns="http://www.w3.org/2000/svg" aria-label="Business card, charcoal version">
    <defs>
      <linearGradient id="zigzag-bright" x1="0" y1="0" x2="1" y2="0">
        <stop offset="0" stop-color="#17a017"/>
        <stop offset="0.55" stop-color="#147a14"/>
        <stop offset="1" stop-color="#2b3a2b"/>
      </linearGradient>
    </defs>
    <rect class="card-face" x="0.5" y="0.5" width="442" height="260" fill="var(--charcoal)" stroke="var(--charcoal-edge)" stroke-width="1"/>
    <polygon class="corner-accent" points="0,0 76,0 0,75" fill="var(--bright-green)" stroke="#4fd04f" stroke-width="1.2"/>
    <polygon class="zigzag" points="163,131 290,131 322,167 317,214 428,214 428,247 288,247 292,172 163,172" fill="url(#zigzag-bright)"/>
    <text class="charcoal-title" x="416" y="42" text-anchor="end">Ray's Coin and Bullion llc .</text>
    <text class="charcoal-info" x="23" y="100">We buy Gold , Silver, Coins &amp; Diamonds.</text>
    <text class="charcoal-info" x="23" y="121">742 Willow Creek road maple ridge vt 08099.</text>
    <text class="charcoal-phone" x="33" y="239">555-555-0148.</text>
    <text class="hours" x="377" y="232" text-anchor="middle">Open 7 days</text>
    <text class="hours" x="377" y="247" text-anchor="middle">9 to 7</text>
  </svg>

</main>
</body>
</html>
```